Professional Home Buyer business card needed

I need a pretty straight forward business card designed. We help people that NEED to sell their homes solve problems. We perform all types of Real Estate transactions including flip, wholesale, investment, rental property and multi family. The card will mainly be used to give to prospective Sellers but will also be given to Real Estate Investors as well. It should professional and very easy to read, most clients are older people.

Target Market(s)

Distressed home sellers as well as Real Estate investors

Industry/Entity Type

Real Estate

Contact Information for Business Card

should be a professional layout

Colors
ec1f27
ffffff
000000

Requirements
Must have
• Large logo on back and smaller one on front. should utilize Red, white, and black.
• I am thinking of using a soft touch coating on the card so keep that in mind.
• Contact info should be very easy to read, think older clients.
Nice to have
• I would like to see a design with rounded corners on the card
Should not have
• pictures of homes or other home graphics.

```html
<!DOCTYPE html>
<html lang="en">
<head>
<meta charset="utf-8">
<title>Summit Property Co – Business Card</title>
<link rel="stylesheet" href="https://fonts.googleapis.com/css2?family=Lato:wght@700;900&display=swap">
<style>
  :root {
    --brand-red: #ec1f27;
    --brand-black: #000000;
    --brand-white: #ffffff;
    --backdrop: #2b2b2b;
  }
  * { box-sizing: border-box; margin: 0; padding: 0; }
  html, body {
    width: 1200px;
    height: 800px;
    overflow: hidden;
    background: var(--backdrop);
    font-family: "Lato", Arial, sans-serif;
  }
  .canvas {
    width: 1200px;
    height: 800px;
    display: flex;
    align-items: center;
    justify-content: center;
    gap: 40px;
  }
  .card {
    position: relative;
    width: 540px;
    height: 310px;
    background: var(--brand-white);
    border-radius: 26px;
    color: var(--brand-black);
    overflow: hidden;
  }

  /* Large name side */
  .card--brand {
    display: flex;
    align-items: center;
    justify-content: center;
  }
  .brand-name {
    display: flex;
    align-items: center;
    gap: 14px;
    font-size: 44px;
    font-weight: 900;
    line-height: 1;
    white-space: nowrap;
  }
  .brand-mark {
    flex: none;
    width: 34px;
    height: 34px;
    background: var(--brand-red);
  }

  /* Contact side */
  .card--contact {
    padding: 34px 40px;
  }
  .contact-list {
    list-style: none;
    display: flex;
    flex-direction: column;
    gap: 6px;
  }
  .contact-list li {
    font-size: 30px;
    font-weight: 700;
    line-height: 1.15;
    padding-bottom: 3px;
    border-bottom: 3px solid var(--brand-red);
    width: fit-content;
  }
  .contact-list li.phone { border-bottom-color: transparent; }
  .brand-name--small {
    position: absolute;
    right: 30px;
    bottom: 30px;
    font-size: 18px;
    gap: 7px;
  }
  .brand-name--small .brand-mark { width: 14px; height: 14px; }
</style>
</head>
<body>
  <main class="canvas">
    <section class="card card--brand" aria-label="Card back with company name">
      <p class="brand-name"><span>Summit Property Co</span><span class="brand-mark" aria-hidden="true"></span></p>
    </section>

    <section class="card card--contact" aria-label="Card front with contact details">
      <ul class="contact-list">
        <li class="name">Dorian Vale</li>
        <li class="role">Maker &amp; Founder</li>
        <li class="email">dorian@valemail.com</li>
        <li class="phone">07700 900 482</li>
      </ul>
      <p class="brand-name brand-name--small"><span>Summit Property Co</span><span class="brand-mark" aria-hidden="true"></span></p>
    </section>
  </main>
</body>
</html>
```